Dorian Walsby Psychotherapy Business Card Design Project

I need a welcoming business card for a Somatic Psychotherapy private practice based in Melbourne, Australia. I help individual clients to work through issues in their life that are inhibiting achieving their full potential. I would like a san serif font and the oculars are:
blue: R:37 G:61 B:95 C:93 M:77 Y:38 K:28
orange: R:241 G:103 B:43 C:0 M:74 Y:93 K:0
The final design should communicate warm, welcoming and safe environment in which clients are supported to grow. It should also convey a collaborative approach to achieve success between me (the therapist) and the client. The uploaded file is my new logo. Also an organic look and feel while maintaining professionalism and a clean, simple look is sought after.
In addition to the logo my details are:
Dorian Walsby
Psychotherapist
B.Arts., Grad Dip. T&D., Dip.Som.Psych, MRKTA, MLOHVB
0417 582 930
dwalsby@dorianwalsby.com.au
www.dorianwalsby.com.au
Target Market(s)
Psychotherapy Clients
Industry/Entity Type
Environment

```html
<!DOCTYPE html>
<html lang="en">
<head>
<meta charset="utf-8">
<title>Dorian Walsby Psychotherapy – Business Card</title>
<link rel="stylesheet" href="https://fonts.googleapis.com/css2?family=Open+Sans:wght@400;600&display=swap">
<style>
  :root {
    --brand-blue: #253d5f;
    --brand-orange: #f1672b;
    --card-white: #ffffff;
    --card-black: #050505;
    --backdrop: #e6e7ea;
    --text-light: #ffffff;
  }
  * { box-sizing: border-box; margin: 0; padding: 0; }
  html, body {
    width: 1200px; height: 900px; overflow: hidden;
    background: var(--backdrop);
    font-family: "Open Sans", Arial, sans-serif;
  }
  .stage {
    position: relative; width: 1200px; height: 900px;
  }
  .card {
    position: absolute; left: 267px; width: 666px; height: 380px;
    overflow: hidden;
    box-shadow: 0 6px 18px rgba(0,0,0,0.18);
  }
  .card-front { top: 50px; background: var(--card-white); }
  .card-back  { top: 470px; background: var(--card-black); }
  .card-band { position: absolute; inset: 0; width: 100%; height: 100%; }

  /* Front */
  .brand-lockup {
    position: absolute; left: 130px; top: 92px;
  }
  .brand-name {
    font-weight: 600; font-size: 34px; line-height: 1.05;
    color: var(--brand-blue); letter-spacing: 0.2px;
  }
  .front-web {
    position: absolute; left: 0; right: 0; top: 318px;
    text-align: center; color: var(--text-light);
    font-size: 22px; letter-spacing: 0.3px;
  }

  /* Back */
  .holder {
    position: absolute; left: 0; right: 0; top: 72px; text-align: center;
  }
  .holder-name {
    color: var(--brand-orange); font-size: 32px; font-weight: 400;
    letter-spacing: 1.5px; line-height: 1;
  }
  .holder-role {
    color: var(--brand-blue); font-size: 20px; font-weight: 600;
    margin-top: 4px; letter-spacing: 0.5px;
  }
  .credentials {
    position: absolute; left: 0; right: 0; top: 188px;
    display: flex; justify-content: center; align-items: center; gap: 12px;
    color: var(--text-light); font-size: 16px;
    list-style: none;
  }
  .credentials li + li::before {
    content: ""; display: inline-block; width: 3px; height: 15px;
    background: var(--text-light); margin-right: 12px; vertical-align: -2px;
  }
  .contact {
    position: absolute; left: 0; right: 0; top: 270px;
    color: var(--text-light); font-size: 17px;
    display: flex; flex-direction: column; align-items: center; gap: 14px;
  }
  .contact-row { display: flex; gap: 36px; }
  .contact-item { display: flex; align-items: center; gap: 8px; }
  .contact-icon { width: 18px; height: 18px; flex: none; }
</style>
</head>
<body>
<main class="stage">

  <section class="card card-front" aria-label="Card front">
    <svg class="card-band" viewBox="0 0 666 380" preserveAspectRatio="none" aria-hidden="true">
      <polygon points="0,292 666,214 666,224 0,302" fill="var(--brand-orange)"/>
      <polygon points="0,306 666,228 666,380 0,380" fill="var(--brand-blue)"/>
    </svg>
    <div class="brand-lockup">
      <span class="brand-name">Dorian Walsby<br>Psychotherapy</span>
    </div>
    <p class="front-web">www.dorianwalsby.com.au</p>
  </section>

  <section class="card card-back" aria-label="Card back">
    <svg class="card-band" viewBox="0 0 666 380" preserveAspectRatio="none" aria-hidden="true">
      <rect x="0" y="238" width="666" height="4" fill="var(--brand-orange)"/>
      <rect x="0" y="242" width="666" height="138" fill="var(--brand-blue)"/>
    </svg>

    <div class="holder">
      <h1 class="holder-name">DORIAN WALSBY</h1>
      <p class="holder-role">Psychotherapist</p>
    </div>

    <ul class="credentials">
      <li>B.Arts.</li>
      <li>Grad Dip. T&amp;D.</li>
      <li>Dip.Som.Psych</li>
      <li>MRKTA</li>
      <li>MLOHVB</li>
    </ul>

    <div class="contact">
      <div class="contact-row">
        <span class="contact-item">
          <svg class="contact-icon" viewBox="0 0 24 24" aria-hidden="true">
            <path d="M6.6 10.8a15 15 0 0 0 6.6 6.6l2.2-2.2c.3-.3.7-.4 1-.2 1.1.4 2.3.6 3.6.6.6 0 1 .4 1 1V20c0 .6-.4 1-1 1A17 17 0 0 1 3 4c0-.6.4-1 1-1h3.5c.6 0 1 .4 1 1 0 1.3.2 2.5.6 3.6.1.3 0 .7-.2 1z" fill="var(--brand-orange)"/>
          </svg>
          0417 582 930
        </span>
        <span class="contact-item">
          <svg class="contact-icon" viewBox="0 0 24 24" aria-hidden="true">
            <rect x="2" y="5" width="20" height="14" fill="none" stroke="var(--brand-orange)" stroke-width="2"/>
            <path d="M2 5l10 8 10-8" fill="none" stroke="var(--brand-orange)" stroke-width="2"/>
          </svg>
          dwalsby@dorianwalsby.com.au
        </span>
      </div>
      <span class="contact-item">
        <svg class="contact-icon" viewBox="0 0 24 24" aria-hidden="true">
          <circle cx="12" cy="12" r="10" fill="var(--brand-orange)"/>
          <path d="M2 12h20M12 2c3 3 3 17 0 20M12 2c-3 3-3 17 0 20" fill="none" stroke="var(--brand-blue)" stroke-width="1.5"/>
        </svg>
        www.dorianwalsby.com.au
      </span>
    </div>
  </section>

</main>
</body>
</html>
```